Mobile technology Business Card Design Project

We need a business card design for our company based in Sydeny Australia, that takes a company's desktop sites and creates a mobile site compatible to all mobile/smartphone devices. This allows greater ease of use and generally faster business conversion than customers using a desktop site.
Our company is called VelqCore but we refer to it as Velq Corestreams. If this could be represented somewhere on the business card that would be great.
Am open to suggestions regarding the colours but a high tech  theme would be good.
Happy bidding!

Target Market(s)
Business owner that has a website and is reasonably savvy regarding online/mobile marketing.
Industry/Entity Type
Business
Requirements
Must have
- Business card details:
Director Peter Langwade
Address: 5/41 Dunmore rd, Kelbrook. 2087
Email: tbc
Web: www.velqcore.com.au
The cards need to have two different names for the two directors.
Gregory Halvane & Peter Langwade (two separate business cards)

```html
<!DOCTYPE html>
<html lang="en">
<head>
<meta charset="utf-8">
<title>VelqCore Business Cards</title>
<link rel="stylesheet" href="https://fonts.googleapis.com/css2?family=Arvo:wght@700&family=Playfair+Display:ital,wght@1,900&display=swap">
<style>
  :root {
    --backdrop: #2b2b2b;
    --card: #f1f1f0;
    --frame: #4a4a4a;
    --ink: #111111;
    --ink-soft: #2a2a2a;
    --icon: #6a6a6a;
    --accent-blue: #2a9ad6;
  }
  * { margin: 0; padding: 0; box-sizing: border-box; }
  html, body {
    width: 1200px; height: 900px; overflow: hidden;
    background: var(--backdrop);
  }
  .canvas {
    position: relative; width: 1200px; height: 900px;
    display: flex; flex-direction: column; align-items: center; justify-content: center; gap: 48px;
  }
  .business-card {
    position: relative; width: 640px; height: 366px;
    background: var(--card); overflow: hidden;
  }
  .card-frame {
    position: absolute; inset: 12px;
    border: 4px solid var(--frame);
  }
  .brand-diamond {
    position: absolute; left: 150px; top: 100px;
    width: 250px; height: 250px;
    transform: translate(-50%, -50%) rotate(45deg);
    background: var(--card);
    border: 7px solid var(--frame);
  }
  .brand-block {
    position: absolute; left: 40px; top: 18px; width: 220px;
    display: flex; flex-direction: column; align-items: center; gap: 12px;
  }
  .brand-dot {
    width: 116px; height: 116px; border-radius: 50%;
    background: var(--accent-blue);
  }
  .brand-name {
    font-family: "Arvo", Georgia, serif; font-weight: 700;
    font-size: 34px; color: var(--ink-soft); letter-spacing: 0.5px;
  }
  .contact-block {
    position: absolute; right: 44px; top: 190px;
    display: flex; flex-direction: column; align-items: flex-end;
  }
  .person-name {
    font-family: "Playfair Display", Georgia, serif; font-style: italic; font-weight: 900;
    font-size: 38px; line-height: 1; color: var(--ink);
  }
  .person-role {
    font-family: "Playfair Display", Georgia, serif; font-style: italic; font-weight: 900;
    font-size: 19px; letter-spacing: 1px; color: var(--ink); margin-top: 2px;
  }
  .detail-list {
    list-style: none; align-self: flex-start; margin-top: 4px; margin-left: -28px;
    font-family: "Arvo", Georgia, serif; font-weight: 700; font-size: 14px;
    text-transform: uppercase; color: var(--ink-soft); letter-spacing: 0.5px;
  }
  .detail-list li { display: flex; align-items: center; gap: 10px; height: 22px; }
  .detail-list .address { margin-left: -4px; }
  .detail-icon { width: 16px; height: 16px; flex: none; }
  .detail-spacer { width: 16px; flex: none; }
</style>
</head>
<body>
<main class="canvas">

  <article class="business-card">
    <div class="card-frame"></div>
    <div class="brand-diamond"></div>
    <div class="brand-block">
      <span class="brand-dot"></span>
      <span class="brand-name">VelqCore</span>
    </div>
    <div class="contact-block">
      <h1 class="person-name">Peter Langwade</h1>
      <p class="person-role">DIRECTOR</p>
      <ul class="detail-list">
        <li class="address"><span class="detail-spacer"></span>5/41 Dunmore rd, Kelbrook. 2087</li>
        <li>
          <svg class="detail-icon" viewBox="0 0 16 16" aria-hidden="true">
            <rect width="16" height="16" rx="2" fill="var(--icon)"/>
            <circle cx="8" cy="8" r="5" fill="none" stroke="#fff" stroke-width="1.2"/>
            <path d="M3 8h10M8 3c-3 3-3 7 0 10M8 3c3 3 3 7 0 10" fill="none" stroke="#fff" stroke-width="1"/>
          </svg>
          www.velqcore.com.au
        </li>
        <li>
          <svg class="detail-icon" viewBox="0 0 16 16" aria-hidden="true">
            <rect width="16" height="16" rx="2" fill="var(--icon)"/>
            <rect x="3" y="4.5" width="10" height="7" fill="none" stroke="#fff" stroke-width="1.2"/>
            <path d="M3 4.5l5 4 5-4" fill="none" stroke="#fff" stroke-width="1.2"/>
          </svg>
          TBC
        </li>
      </ul>
    </div>
  </article>

  <article class="business-card">
    <div class="card-frame"></div>
    <div class="brand-diamond"></div>
    <div class="brand-block">
      <span class="brand-dot"></span>
      <span class="brand-name">VelqCore</span>
    </div>
    <div class="contact-block">
      <h1 class="person-name">Gregory Halvane</h1>
      <p class="person-role">DIRECTOR</p>
      <ul class="detail-list">
        <li class="address"><span class="detail-spacer"></span>5/41 Dunmore rd, Kelbrook. 2087</li>
        <li>
          <svg class="detail-icon" viewBox="0 0 16 16" aria-hidden="true">
            <rect width="16" height="16" rx="2" fill="var(--icon)"/>
            <circle cx="8" cy="8" r="5" fill="none" stroke="#fff" stroke-width="1.2"/>
            <path d="M3 8h10M8 3c-3 3-3 7 0 10M8 3c3 3 3 7 0 10" fill="none" stroke="#fff" stroke-width="1"/>
          </svg>
          www.velqcore.com.au
        </li>
        <li>
          <svg class="detail-icon" viewBox="0 0 16 16" aria-hidden="true">
            <rect width="16" height="16" rx="2" fill="var(--icon)"/>
            <rect x="3" y="4.5" width="10" height="7" fill="none" stroke="#fff" stroke-width="1.2"/>
            <path d="M3 4.5l5 4 5-4" fill="none" stroke="#fff" stroke-width="1.2"/>
          </svg>
          TBC
        </li>
      </ul>
    </div>
  </article>

</main>
</body>
</html>
```